Reed & Vale NC grand opening (for BILLBOARD)

Advertising the grand opening of our cannabis/hemp shop in NC. We will sell all things hemp (flower, cartridges, disposables, edibles, creams, lotions, pet products etc...)

Requirements
Must have
• include, open starting Aug 1, but grand opening Aug 15th.
Nice to have
• Difference slogan ideas "Save some cash, buy our grass" "Find your perfect high at Reed & Vale cannabis store" "Experience Nature's Gift: Reed & Vale Cannabis Store"

```html
<!DOCTYPE html>
<html lang="en">
<head>
<meta charset="utf-8">
<title>Reed &amp; Vale Cannabis Store – Billboard</title>
<link rel="stylesheet" href="https://fonts.googleapis.com/css2?family=Archivo:ital,wdth,wght@0,62..125,100..900;1,62..125,100..900&display=swap">
<style>
  :root {
    --page: #ffffff;
    --navy: #141a3d;
    --deep-teal: #0f4a52;
    --teal: #13665e;
    --leaf-green: #7cc242;
    --forest: #17673a;
    --pill: #10b09a;
    --white: #ffffff;
  }
  * { margin: 0; padding: 0; box-sizing: border-box; }
  html, body {
    width: 1191px;
    height: 1200px;
    overflow: hidden;
    background: var(--page);
  }
  .billboard {
    position: absolute;
    left: 40px;
    top: 437px;
    width: 1111px;
    height: 325px;
    overflow: hidden;
    background:
      radial-gradient(ellipse 420px 150px at 330px 150px, rgba(19, 110, 96, 0.75), transparent 70%),
      linear-gradient(100deg, var(--navy) 0%, var(--deep-teal) 45%, var(--teal) 62%, #123a55 78%, var(--navy) 100%);
    font-family: "Archivo", "Helvetica Neue", Arial, sans-serif;
    font-stretch: 125%;
    color: var(--white);
  }
  .foliage {
    position: absolute;
    right: 0;
    top: 0;
    width: 330px;
    height: 100%;
    background:
      radial-gradient(ellipse 260px 120px at 210px 95px, var(--leaf-green) 0%, rgba(124, 194, 66, 0.55) 55%, transparent 80%),
      radial-gradient(ellipse 230px 90px at 260px 290px, var(--forest) 0%, rgba(124, 194, 66, 0.5) 50%, transparent 80%),
      linear-gradient(90deg, transparent 0%, rgba(23, 103, 58, 0.6) 40%, var(--forest) 100%);
  }
  .headline {
    position: absolute;
    left: 42px;
    top: 52px;
    font-style: italic;
    font-weight: 800;
    text-transform: uppercase;
    line-height: 1;
    white-space: nowrap;
  }
  .headline .kicker {
    display: block;
    font-size: 30px;
    font-weight: 600;
    margin-bottom: 8px;
  }
  .headline .main {
    display: block;
    font-size: 60px;
    letter-spacing: -0.5px;
    margin-bottom: 2px;
  }
  .headline .brand { color: var(--leaf-green); }
  .headline .store {
    display: block;
    font-size: 60px;
    letter-spacing: -0.5px;
  }
  .exit-pill {
    position: absolute;
    left: 38px;
    top: 230px;
    width: 372px;
    height: 41px;
    border-radius: 21px;
    background: var(--pill);
    display: flex;
    align-items: center;
    justify-content: center;
    font-style: italic;
    font-weight: 600;
    font-size: 20px;
    text-transform: uppercase;
    white-space: nowrap;
  }
  .opening-dates {
    position: absolute;
    left: 42px;
    top: 286px;
    font-style: italic;
    font-weight: 600;
    font-size: 17px;
    text-transform: uppercase;
    letter-spacing: 0.3px;
    white-space: nowrap;
  }
  .opening-dates .grand { color: var(--leaf-green); }
  .wordmark {
    position: absolute;
    left: 483px;
    top: 222px;
    display: flex;
    align-items: center;
    gap: 14px;
    color: var(--leaf-green);
    font-weight: 600;
    font-size: 56px;
    font-stretch: 100%;
    letter-spacing: -0.5px;
    line-height: 1;
    white-space: nowrap;
  }
  .wordmark .dot {
    width: 22px;
    height: 22px;
    border-radius: 50%;
    background: var(--leaf-green);
  }
</style>
</head>
<body>
  <section class="billboard">
    <div class="foliage" role="img" aria-label="Large stylised green leaf blades sweeping in from the right edge"></div>

    <h1 class="headline">
      <span class="kicker">Experience Nature's Gift:</span>
      <span class="main"><span class="brand">Reed &amp; Vale</span> Cannabis</span>
      <span class="store">Store</span>
    </h1>

    <div class="exit-pill">Exit 4B Maple Grove Rd</div>

    <p class="opening-dates">Open from Aug 1 · <span class="grand">Grand Opening Aug 15</span></p>

    <div class="wordmark">
      <span class="dot"></span>
      <span class="name">Reed &amp; Vale</span>
    </div>
  </section>
</body>
</html>
```